Bidwell+ WordPress Design

We need a wordpress design that will incorporate a professional color scheme with company logo in a clean layout. The design needs to consider that this will be developed on a responsive theme. Colors are up to the designer - The red of the logo with black, gray or an accent color (maybe the purple of in the photos). Client wants a 'modern' look.

Industry/Entity Type

It Company

Number of Pages Required

1 page

Font styles to use
Serif
Sans Serif

Requirements
Must have
• Navigation: 1) Home 2) Our Auctions 3) Services 4) Buyers & Sellers 5) About Us 6) Contact Us
• Colors - a corporate look with professional color scheme. Red of logo + black and gray, or any other accent that keeps a corporate look. (purple if it looks good)
• In header - logo (attached) , and contact info
• Phone: 555-304-7261 / 555-618-9042
• eMail: hollisbids@maplewire.example
• bidwellplusregion@maplewire.example
• Address: 6217 W Route 842 • Dunmore, TX 70419
• Design will feature a slideshow either full width (960 px) or in the content area - images attached.
• Widgets in sidebar or where appropriate - 1) Email Signup 2) Upcoming Auctions 4) News&Events blog 5) Testimonials 6) Social media - FB, RSS
• Footer will have company logo, association logos (attached) and contact info, with another widget area if necessary
Nice to have
• Use of dropdown menus:
• 1) News&Events and 2) Testimonials under About Us

```html
<!DOCTYPE html>
<html lang="en">
<head>
<meta charset="utf-8">
<title>Bidwell+ | Auctions</title>
<link href="https://fonts.googleapis.com/css2?family=Open+Sans:ital,wght@0,400;0,600;0,700;1,400&display=swap" rel="stylesheet">
<style>
:root{
  --red:#e2141b;
  --red-dark:#b80f15;
  --ink:#1c1c1c;
  --text:#555;
  --muted:#9a9a9a;
  --line:#e2e2e2;
  --footer:#ececec;
  --bottom:#1e1e1e;
  --white:#fff;
}
*{margin:0;padding:0;box-sizing:border-box}
html,body{width:1200px;height:2605px;overflow:hidden;background:var(--white);font-family:"Open Sans",Arial,sans-serif;color:var(--text)}
.page{position:relative;width:1200px;height:2605px}
.abs{position:absolute}

/* header */
.logo{font-weight:700;color:var(--ink);font-size:34px;letter-spacing:-.5px;display:flex;align-items:center;gap:8px}
.logo .dot{width:12px;height:12px;background:var(--red)}
.site-logo{left:99px;top:36px}
.header-info{font-size:12.5px;line-height:21px;color:#444}
.header-mail{left:580px;top:31px}
.header-phone{left:820px;top:31px}

/* nav */
.main-nav{left:0;top:115px;width:1200px;height:55px;background:var(--red);box-shadow:inset 0 -2px 0 var(--red-dark)}
.main-nav ul{list-style:none;position:absolute;left:99px;top:0;display:flex;height:55px}
.main-nav li{height:55px;display:flex;align-items:center;justify-content:center;color:var(--white);font-size:13px;text-transform:uppercase;border-right:1px solid rgba(0,0,0,.15)}
.main-nav li.active{background:#111}
.dropdown{left:811px;top:170px;width:163px;height:73px;background:#1a1a1a;padding:10px 15px;font-size:12px;color:var(--white);line-height:27px}

/* slider */
.hero{left:0;top:170px;width:1200px;height:511px;background:linear-gradient(180deg,#b9b8b4 0%,#8d8a86 40%,#5a4f6e 70%,#6c6a72 100%)}
.hero-arrow{left:14px;top:398px}
.hero-dots{left:588px;top:645px;display:flex;gap:6px}
.hero-dots span{width:12px;height:12px;border-radius:50%;border:2px solid var(--white)}
.hero-dots span.on{background:var(--red);border-color:var(--red)}

/* headings */
.section-title{font-size:23px;font-weight:700;color:var(--ink);text-transform:uppercase}
.side-title{font-size:16px;font-weight:700;color:var(--ink);text-transform:uppercase}

/* cards */
.cards{left:99px;width:726px;display:grid;grid-template-columns:repeat(3,219px);column-gap:33px}
.card .photo{height:156px;border:3px solid #eee}
.card-title{margin-top:20px;font-size:11px;font-weight:700;color:#555;text-transform:uppercase}
.card-loc{font-size:11.5px;color:var(--red);margin-top:4px}
.card-loc span{color:var(--text)}
.card-text{font-size:11.5px;color:var(--muted);line-height:20px;margin-top:4px}
.btn{display:inline-block;background:var(--red);color:var(--white);font-size:11px;font-weight:700;text-transform:uppercase;padding:0 18px;height:31px;line-height:31px;border-bottom:2px solid var(--red-dark)}
.card .btn{margin-top:14px}

/* blog */
.photo{background:linear-gradient(135deg,#ddd 0%,#b9b4ad 100%)}
.blog-post{position:absolute}
.post-title{font-size:11px;font-weight:700;color:#555;text-transform:uppercase;line-height:22px}
.meta{display:flex;gap:22px;font-size:11px;color:#c4c4c4;align-items:center}
.meta span{display:flex;align-items:center;gap:7px}
.post-text{font-size:11.5px;color:var(--muted);line-height:20px}

/* sidebar */
.sidebar{left:882px;width:220px}
.side-text{font-size:11.5px;color:var(--muted);line-height:21px}
.email-input{width:217px;height:35px;border:1px solid #ddd;font-size:11px;color:#bbb;padding:0 10px;line-height:33px}
.feed-item{position:absolute;left:0;display:flex;gap:14px}
.avatar{width:66px;height:66px;background:linear-gradient(160deg,#d9cfc5,#8f8478)}
.feed-head{font-size:11.5px;color:#444;line-height:18px}
.feed-sub{font-size:10.5px;color:var(--muted);line-height:18px}
.feed-date{font-size:10px;color:#777;display:flex;gap:9px;align-items:center;margin-top:6px}
.quote{font-size:11.5px;font-style:italic;color:var(--muted);line-height:21px}
.quote-name{font-size:11.5px;font-weight:700;color:var(--red)}

/* footer */
.footer{left:0;top:2296px;width:1200px;height:233px;background:var(--footer)}
.footer h3{font-size:19px;font-weight:700;color:var(--ink);text-transform:uppercase}
.footer-col{position:absolute;top:56px}
.footer-divider{position:absolute;top:40px;width:1px;height:160px;background:#d6d6d6}
.footer-text{font-size:11.5px;color:#777;line-height:21px}
.footer-text b{color:var(--red);font-weight:600}
.badges{display:flex;align-items:center;gap:22px;margin-top:22px}
.badge-circle{width:62px;height:62px;border-radius:50%;background:#2a2a2a}
.badge-square{width:52px;height:52px;background:#2a2a2a}
.footer .logo{font-size:22px}
.footer .logo .dot{width:9px;height:9px}
.bottom-bar{left:0;top:2529px;width:1200px;height:76px;background:var(--bottom);font-size:11px;color:#bbb}
.copyright{position:absolute;left:103px;top:31px}
.foot-nav{position:absolute;left:640px;top:31px;display:flex;gap:10px}
.foot-nav i{font-style:normal;color:#666}
</style>
</head>
<body>
<div class="page">

  <header>
    <div class="abs site-logo logo">Bidwell+<span class="dot"></span></div>
    <div class="abs header-info header-mail">eMail: hollisbids@maplewire.example<br>bidwellplusregion@maplewire.example</div>
    <div class="abs header-info header-phone">Phone: 555-304-7261 / 555-618-9042<br>Address: 6217 W Route 842 • Dunmore, TX 70419</div>
  </header>

  <nav class="abs main-nav">
    <ul>
      <li class="active" style="width:92px">Home</li>
      <li style="width:222px">Our Auctions</li>
      <li style="width:145px">Services</li>
      <li style="width:223px">Buyers &amp; Sellers</li>
      <li style="width:160px">About Us</li>
      <li style="width:162px;border-right:0">Contact Us</li>
    </ul>
  </nav>

  <section class="abs hero" role="img" aria-label="Slideshow photo of the auction team in purple shirts pointing toward the bidders"></section>
  <div class="abs dropdown"><div>News &amp; Events</div><div>Testimonials</div></div>
  <svg class="abs hero-arrow" width="44" height="44" viewBox="0 0 44 44"><circle cx="22" cy="22" r="20" fill="none" stroke="#fff" stroke-width="1.5" opacity=".8"/><path d="M25 14l-8 8 8 8" fill="none" stroke="#fff" stroke-width="2"/></svg>
  <div class="abs hero-dots"><span class="on"></span><span></span></div>

  <!-- upcoming auctions -->
  <h2 class="abs section-title" style="left:99px;top:708px">Upcoming Auctions</h2>

  <div class="abs cards" style="top:773px">
    <article class="card"><div class="photo" role="img" aria-label="White sofa in a bright living room"></div><div class="card-title">For Sale - 5.63 Wooded Acres</div><div class="card-loc">Location: <span>Fenwick Rd, GA 30491</span></div><p class="card-text">Lorem Ipsum is simply dummy text of the printing alorndsetting industry.</p><span class="btn">For Sale</span></article>
    <article class="card"><div class="photo" role="img" aria-label="Brown leather wingback armchair" style="background:linear-gradient(135deg,#e2ddd6,#6b5443)"></div><div class="card-title">For Sale - 5.63 Wooded Acres</div><div class="card-loc">Location: <span>Fenwick Rd, GA 30491</span></div><p class="card-text">Lorem Ipsum is simply dummy text of the printing alorndsetting industry.</p><span class="btn">For Sale</span></article>
    <article class="card"><div class="photo" role="img" aria-label="Orange and cream lounge furniture set" style="background:linear-gradient(135deg,#f6f2ea,#e39a4c)"></div><div class="card-title">For Sale - 5.63 Wooded Acres</div><div class="card-loc">Location: <span>Fenwick Rd, GA 30491</span></div><p class="card-text">Lorem Ipsum is simply dummy text of the printing alorndsetting industry.</p><span class="btn">For Sale</span></article>
  </div>

  <div class="abs cards" style="top:1108px">
    <article class="card"><div class="photo" role="img" aria-label="Cream sofa with cushions" style="background:linear-gradient(135deg,#f1ece4,#c8bca8)"></div><div class="card-title">For Sale - 5.63 Wooded Acres</div><div class="card-loc">Location: <span>Fenwick Rd, GA 30491</span></div><p class="card-text">Lorem Ipsum is simply dummy text of the printing alorndsetting industry.</p><span class="btn">For Sale</span></article>
    <article class="card"><div class="photo" role="img" aria-label="Dark wicker patio furniture by a pool" style="background:linear-gradient(180deg,#8fb2b8,#3a3d42)"></div><div class="card-title">For Sale - 5.63 Wooded Acres</div><div class="card-loc">Location: <span>Fenwick Rd, GA 30491</span></div><p class="card-text">Lorem Ipsum is simply dummy text of the printing alorndsetting industry.</p><span class="btn">For Sale</span></article>
    <article class="card"><div class="photo" role="img" aria-label="Blue grey sofa in a modern room" style="background:linear-gradient(180deg,#e4e4e6,#4b5568)"></div><div class="card-title">For Sale - 5.63 Wooded Acres</div><div class="card-loc">Location: <span>Fenwick Rd, GA 30491</span></div><p class="card-text">Lorem Ipsum is simply dummy text of the printing alorndsetting industry.</p><span class="btn">For Sale</span></article>
  </div>

  <!-- news & events -->
  <h2 class="abs section-title" style="left:97px;top:1451px">News &amp; Events Blog</h2>

  <article class="blog-post" style="left:99px;top:1502px;width:342px">
    <div class="photo" style="height:174px;border:3px solid #eee" role="img" aria-label="White modern kitchen and living area"></div>
    <div class="post-title" style="margin-top:15px">For Sale - 5.63 Wooded Acres</div>
    <div class="meta" style="margin-top:13px">
      <span><svg width="11" height="11" viewBox="0 0 11 11"><rect x=".5" y="1.5" width="10" height="9" fill="#ccc"/><rect x="2" y="4" width="7" height="5" fill="#fff"/></svg>June 3 , 2013</span>
      <span><svg width="12" height="11" viewBox="0 0 12 11"><path d="M0 0h12v8H4l-3 3V8H0z" fill="#ccc"/></svg>12 Comments</span>
      <span><svg width="9" height="12" viewBox="0 0 9 12"><path d="M4.5 0A4.5 4.5 0 0 0 0 4.5C0 8 4.5 12 4.5 12S9 8 9 4.5A4.5 4.5 0 0 0 4.5 0zm0 6.3a1.8 1.8 0 1 1 0-3.6 1.8 1.8 0 0 1 0 3.6z" fill="#ccc"/></svg>Location</span>
    </div>
    <p class="post-text" style="margin-top:13px">Lorem Ipsum is simply dummy text of the printing alorndsetting industry orem Ipsum hlorea.</p>
  </article>

  <article class="blog-post" style="left:478px;top:1502px;width:343px">
    <div class="photo" style="height:174px;border:3px solid #eee;background:linear-gradient(180deg,#f3f1ef 50%,#c4302c 75%,#efe9e4)" role="img" aria-label="Red sectional sofa in a white lounge"></div>
    <div class="post-title" style="margin-top:15px">For Sale - 5.63 Wooded Acres</div>
    <div class="meta" style="margin-top:13px">
      <span><svg width="11" height="11" viewBox="0 0 11 11"><rect x=".5" y="1.5" width="10" height="9" fill="#ccc"/><rect x="2" y="4" width="7" height="5" fill="#fff"/></svg>June 3 , 2013</span>
      <span><svg width="12" height="11" viewBox="0 0 12 11"><path d="M0 0h12v8H4l-3 3V8H0z" fill="#ccc"/></svg>12 Comments</span>
      <span><svg width="9" height="12" viewBox="0 0 9 12"><path d="M4.5 0A4.5 4.5 0 0 0 0 4.5C0 8 4.5 12 4.5 12S9 8 9 4.5A4.5 4.5 0 0 0 4.5 0zm0 6.3a1.8 1.8 0 1 1 0-3.6 1.8 1.8 0 0 1 0 3.6z" fill="#ccc"/></svg>Location</span>
    </div>
    <p class="post-text" style="margin-top:13px">Lorem Ipsum is simply dummy text of the printing alorndsetting industry orem Ipsum hlorea.</p>
  </article>

  <article class="blog-post" style="left:99px;top:1827px;width:723px">
    <div class="photo" style="height:208px;border:3px solid #eee;background:linear-gradient(90deg,#8b8680,#5c4c72 40%,#b8b4ad 70%,#6e6590)" role="img" aria-label="Auctioneers in purple shirts calling bids inside a warehouse"></div>
    <div class="post-title" style="margin-top:24px">Sed ut perspiciatis unde omnis iste natus error sit voluptatem accusantium doloremque laudantiumt, consectetur, adipisci velit, sed quia no</div>
    <div class="meta" style="margin-top:10px">
      <span><svg width="11" height="11" viewBox="0 0 11 11"><rect x=".5" y="1.5" width="10" height="9" fill="#ccc"/><rect x="2" y="4" width="7" height="5" fill="#fff"/></svg>June 3 , 2013</span>
      <span><svg width="12" height="11" viewBox="0 0 12 11"><path d="M0 0h12v8H4l-3 3V8H0z" fill="#ccc"/></svg>12 Comments</span>
      <span><svg width="9" height="12" viewBox="0 0 9 12"><path d="M4.5 0A4.5 4.5 0 0 0 0 4.5C0 8 4.5 12 4.5 12S9 8 9 4.5A4.5 4.5 0 0 0 4.5 0zm0 6.3a1.8 1.8 0 1 1 0-3.6 1.8 1.8 0 0 1 0 3.6z" fill="#ccc"/></svg>Location</span>
    </div>
    <p class="post-text" style="margin-top:12px">Lorem Ipsum is simply dummy text of the printing alorndsetting industry. Lorem Ipsum hloreas bee tronic typesetting, rema ining essentially unchangedThere are many variations of passages of Lorem Ipsum available,.</p>
    <span class="btn" style="margin-top:10px">Read More</span>
  </article>

  <!-- sidebar -->
  <aside class="abs sidebar" style="top:712px;height:1440px">
    <h3 class="side-title">Email Signup</h3>
    <p class="side-text" style="margin-top:10px">Subscribe to receive inspiration, ideas and news in your inbox</p>
    <div class="email-input" style="margin-top:8px">Your email address</div>
    <span class="btn" style="margin-top:13px;height:35px;line-height:33px;padding:0 17px">Subscribe</span>

    <h3 class="side-title abs" style="top:216px">Chatterbox Feeds</h3>
    <div class="feed-item" style="top:260px"><div class="avatar" role="img" aria-label="Member portrait"></div><div><div class="feed-head">Standard Post with Theg.</div><div class="feed-sub">Lorem Ipsum isloremsim</div><div class="feed-date"><svg width="11" height="11" viewBox="0 0 11 11"><rect x=".5" y="1.5" width="10" height="9" fill="#999"/><rect x="2" y="4" width="7" height="5" fill="#fff"/></svg>21 March 2013</div></div></div>
    <div class="feed-item" style="top:350px"><div class="avatar" role="img" aria-label="Member portrait"></div><div><div class="feed-head">Standard Post with Theg.</div><div class="feed-sub">Lorem Ipsum isloremsim</div><div class="feed-date"><svg width="11" height="11" viewBox="0 0 11 11"><rect x=".5" y="1.5" width="10" height="9" fill="#999"/><rect x="2" y="4" width="7" height="5" fill="#fff"/></svg>21 March 2013</div></div></div>
    <div class="feed-item" style="top:438px"><div class="avatar" role="img" aria-label="Member portrait"></div><div><div class="feed-head">Standard Post with Theg.</div><div class="feed-sub">Lorem Ipsum isloremsim</div><div class="feed-date"><svg width="11" height="11" viewBox="0 0 11 11"><rect x=".5" y="1.5" width="10" height="9" fill="#999"/><rect x="2" y="4" width="7" height="5" fill="#fff"/></svg>21 March 2013</div></div></div>
    <div class="feed-item" style="top:527px"><div class="avatar" role="img" aria-label="Member portrait"></div><div><div class="feed-head">Standard Post with Theg.</div><div class="feed-sub">Lorem Ipsum isloremsim</div><div class="feed-date"><svg width="11" height="11" viewBox="0 0 11 11"><rect x=".5" y="1.5" width="10" height="9" fill="#999"/><rect x="2" y="4" width="7" height="5" fill="#fff"/></svg>21 March 2013</div></div></div>

    <h3 class="side-title abs" style="top:645px">RSS Feeds</h3>
    <div class="feed-item" style="top:684px"><div><div class="feed-head">SLore mipsum dolor sir solor with lore.</div><div class="feed-sub">Lorem Ipsum isloremsim</div><div class="feed-date"><svg width="11" height="11" viewBox="0 0 11 11"><rect x=".5" y="1.5" width="10" height="9" fill="#999"/><rect x="2" y="4" width="7" height="5" fill="#fff"/></svg>21 March 2013</div></div></div>
    <div class="feed-item" style="top:764px"><div><div class="feed-head">SLore mipsum dolor sir solor with lore.</div><div class="feed-sub">Lorem Ipsum isloremsim</div><div class="feed-date"><svg width="11" height="11" viewBox="0 0 11 11"><rect x=".5" y="1.5" width="10" height="9" fill="#999"/><rect x="2" y="4" width="7" height="5" fill="#fff"/></svg>21 March 2013</div></div></div>
    <div class="feed-item" style="top:844px"><div><div class="feed-head">SLore mipsum dolor sir solor with lore.</div><div class="feed-sub">Lorem Ipsum isloremsim</div><div class="feed-date"><svg width="11" height="11" viewBox="0 0 11 11"><rect x=".5" y="1.5" width="10" height="9" fill="#999"/><rect x="2" y="4" width="7" height="5" fill="#fff"/></svg>21 March 2013</div></div></div>
    <div class="feed-item" style="top:924px"><div><div class="feed-head">SLore mipsum dolor sir solor with lore.</div><div class="feed-sub">Lorem Ipsum isloremsim</div><div class="feed-date"><svg width="11" height="11" viewBox="0 0 11 11"><rect x=".5" y="1.5" width="10" height="9" fill="#999"/><rect x="2" y="4" width="7" height="5" fill="#fff"/></svg>21 March 2013</div></div></div>

    <h3 class="side-title abs" style="top:1030px">Testimonials</h3>
    <div class="abs" style="top:1072px;left:0;width:220px">
      <p class="quote">“ Sed ut perspiciatis unde omnis iste natus error sit voluptatem accusantium dolo remque laudantium, totam rem ap e ria m, eaque ipsa quao ab illo invento re veritatis et quasi architecto”</p>
      <p class="quote-name" style="margin-top:14px">Mara Quill, City Name</p>
      <p class="quote" style="margin-top:18px">“ Sed ut perspiciatis unde omnis iste natus error sit voluptatem accusantium dolo remque laudantium, totam rem ap e ria m, eaque ipsa quao ab illo invento re veritatis et quasi architecto”</p>
      <p class="quote-name" style="margin-top:14px">Mara Quill, City Name</p>
      <p class="quote-name" style="margin-top:16px;font-weight:600;padding-left:6px">Read More</p>
    </div>
  </aside>

  <!-- footer -->
  <footer class="abs footer">
    <div class="footer-col" style="left:102px;width:300px">
      <h3>Associations</h3>
      <div class="badges">
        <div class="badge-circle" role="img" aria-label="Association badge"></div>
        <div class="badge-square" role="img" aria-label="Association badge"></div>
        <div class="logo">Bidwell+<span class="dot"></span></div>
      </div>
    </div>
    <div class="footer-divider" style="left:427px"></div>
    <div class="footer-col" style="left:472px;width:320px">
      <h3>About Us</h3>
      <p class="footer-text" style="margin-top:14px">Lorem ipsum dolor sit amet, consectetuer adipiscing elit. Praesent vestibulum molestie lacuAenean</p>
      <p class="footer-text" style="margin-top:12px">Lorem ipsum dolor sit amet, consectetuer adipiscing elit. Praesent vestibulum molestie lacuAenean</p>
    </div>
    <div class="footer-divider" style="left:821px"></div>
    <div class="footer-col" style="left:880px;width:240px">
      <h3>Contact Info</h3>
      <p class="footer-text" style="margin-top:12px">Phone: <b>555-304-7261 / 555-618-9042</b><br>eMail: hollisbids@maplewire.example<br>bidwellplusregion@maplewire.example<br>Address: 6217 W Route 842 • Dunmore, TX 70419</p>
    </div>
  </footer>

  <div class="abs bottom-bar">
    <div class="copyright">© 2014 Bidwell+. All Rights Reserved. Listings Site Map</div>
    <div class="foot-nav"><span>Home</span><i>|</i><span>Our Auctions</span><i>|</i><span>Services</span><i>|</i><span>Buyers &amp; Sellers</span><i>|</i><span>About Us</span><i>|</i><span>Contact Us</span></div>
  </div>

</div>
</body>
</html>
```